Velcrest-Aura

Letter heads, business cards, packaging envelopes big and small, and stationery
We have logo design and trademarked approval, we would lie to
upload design to help create this project.
This product was created for my Mother a 4 time diganosed Cancer
Survivor, This product has patent pending and now will be offered to the general public as well.
We are looking foward to working with all of you as this product
and stationary will be viewed worldwide.
Thanks
The Kindale Family

Target Market(s)

all ages and worldwide

Industry/Entity Type

Business

Requirements
Must have
• Our Logo

```html
<!DOCTYPE html>
<html lang="en">
<head>
<meta charset="utf-8">
<title>Velcrest-Aura Envelope</title>
<link rel="stylesheet" href="https://fonts.googleapis.com/css2?family=Montserrat:wght@800&family=Arimo:wght@400&display=swap">
<style>
  :root {
    --backdrop: #e9e7e3;
    --paper: #ffffff;
    --navy: #0d3a72;
    --red: #d0202e;
    --ink: #3a3a3a;
  }
  html, body {
    margin: 0;
    width: 1200px;
    height: 720px;
    overflow: hidden;
    background: var(--backdrop);
  }
  .envelope {
    position: absolute;
    left: 130px;
    top: 140px;
    width: 940px;
    height: 440px;
    background: var(--paper);
    box-shadow: 0 6px 24px rgba(0,0,0,0.18);
  }
  .brand {
    position: absolute;
    left: 34px;
    top: 34px;
    display: flex;
    align-items: center;
    gap: 8px;
  }
  .brand-dot {
    width: 22px;
    height: 22px;
    border-radius: 50%;
    background: var(--red);
  }
  .brand-name {
    font-family: "Montserrat", sans-serif;
    font-weight: 800;
    font-size: 27px;
    color: var(--navy);
    letter-spacing: -0.5px;
    line-height: 1;
  }
  .sender {
    position: absolute;
    left: 42px;
    top: 92px;
    font-family: "Arimo", sans-serif;
    font-size: 11px;
    line-height: 14px;
    color: var(--ink);
  }
  .sender-web {
    color: var(--red);
  }
  .base-band {
    position: absolute;
    left: 0;
    right: 0;
    bottom: 16px;
    height: 20px;
    background: var(--navy);
  }
</style>
</head>
<body>
  <div class="envelope">
    <div class="brand">
      <span class="brand-dot"></span>
      <span class="brand-name">Velcrest-Aura</span>
    </div>
    <div class="sender">
      <div>PO Box 418</div>
      <div>Ferndale NSW 2150</div>
      <div class="sender-web">www.velcrest-aura.com</div>
    </div>
    <div class="base-band"></div>
  </div>
</body>
</html>
```